Corsets, Cups and Commerce needs a book cover

I've been in lingerie business for 12 years, we own 5 x Lingerie stores. This is my story aimed at women in business or women who want to start a business. Essentially its a business book but also offers bra fitting advice. Although the book cover can be a bit cheeky it also needs to be tasteful. I do not have a colour in mind I just don't like it too girly. I like strong and bold with a feminine touch. The title needs to catch peoples attention when surrounded by so many other books. It needs to have some sort of image or texture. That could be a lace background texture. I like the idea of a bra hanging off the letters or some kind of image of a bra but a beautiful lacy bra. I would like the cover to be more beautiful than tacky even though it has the word 'boobs'.
Updates

Hi everyone, some great designs so far. Many of you have made a bra part of the 'Boobs' word. I thought this could work but it doesn't as it covers up the word 'Boobs' too much and I feel this word will catch peoples attention. If any of you would like to revise please feel free. thankyou Delphine.

Target Market(s)

Women in business or women wanting to start a business.

Industry/Entity Type

Retail

Logo Text

Corsets, Cups and Commerce

Font styles to use
Serif
Sans Serif

Colors

Designer to choose colors to be used in the design.

Requirements
Must have
• Title: Corsets, Cups and Commerce (you could replace 'and' with '&' if it works better.
• Tagline: Steady Lessons for Women in Trade
• Author: Delphine Karsby
Nice to have
• An image of a bra, maybe in a playful way. It could hang off the letters or maybe the letters could look like a bra, but I'm concerned it may look tacky that way. Somehow incorporate a picture of a bra preferably as part of the title.
• I don't have images for you, you have the freedom to choose.
Should not have
• Although this book has boobs and bras in the title it must not be tacky or sexual. It is a business book.
• I do not like it to look too girly, probably not script unless its subtle.

```html
<!DOCTYPE html>
<html lang="en">
<head>
<meta charset="utf-8">
<title>Corsets, Cups &amp; Commerce — Cover Options</title>
<link rel="stylesheet" href="https://fonts.googleapis.com/css2?family=Alegreya+SC:wght@700&family=Barlow+Condensed:wght@400;500&display=swap">
<style>
  :root {
    --stage: #1a1e1e;
    --paper: #fbfcfb;
    --ink: #111111;
    --signal-red: #fb2e0a;
    --cream: #f5f6b2;
    --icon-light: #e4e4e4;
    --icon-warm: #ff6a4a;
  }
  * { margin: 0; padding: 0; box-sizing: border-box; }
  html, body {
    width: 1200px;
    height: 912px;
    overflow: hidden;
    background: var(--stage);
  }
  .stage {
    position: relative;
    width: 1200px;
    height: 912px;
  }
  .cover {
    position: absolute;
    top: 101px;
    width: 500px;
    height: 713px;
    box-shadow: 0 10px 30px rgba(0,0,0,0.45);
    text-align: center;
  }
  .cover--white { left: 62px; background: var(--paper); color: var(--ink); }
  .cover--red { left: 633px; background: var(--signal-red); color: var(--cream); }

  .author {
    position: absolute;
    left: 0; right: 0;
    font-family: "Barlow Condensed", sans-serif;
    font-weight: 500;
    font-size: 28px;
    line-height: 1;
  }
  .cover--white .author { top: 66px; }
  .cover--red .author { top: 50px; }

  .title {
    position: absolute;
    left: 0; right: 0;
    font-family: "Alegreya SC", serif;
    font-weight: 700;
  }
  .title span { display: block; }
  .cover--white .title { top: 254px; font-size: 62px; line-height: 88px; }
  .cover--red .title { top: 194px; font-size: 70px; line-height: 83px; }

  .bra-mark {
    position: absolute;
    display: block;
    border-radius: 0 0 48px 48px;
  }
  .cover--white .bra-mark { left: 202px; top: 483px; width: 98px; height: 74px; background: var(--icon-light); }
  .cover--red .bra-mark { left: 197px; top: 609px; width: 106px; height: 68px; background: var(--icon-warm); }

  .tagline {
    position: absolute;
    left: 0; right: 0;
    font-family: "Barlow Condensed", sans-serif;
    font-weight: 400;
  }
  .cover--white .tagline {
    top: 625px;
    font-size: 26px;
    text-transform: uppercase;
    letter-spacing: 0.2px;
  }
  .tagline-band {
    position: absolute;
    left: 0; right: 0;
    top: 569px;
    height: 40px;
    background: var(--cream);
  }
  .cover--red .tagline {
    top: 569px;
    height: 40px;
    line-height: 40px;
    font-size: 26px;
    font-weight: 500;
    color: var(--signal-red);
  }
</style>
</head>
<body>
<main class="stage">
  <section class="cover cover--white">
    <p class="author">Delphine Karsby</p>
    <h1 class="title"><span>Corsets, Cups</span><span>&amp; Commerce</span></h1>
    <div class="bra-mark" role="img" aria-label="Line icon of a lace bra"></div>
    <p class="tagline">Steady Lessons for Women in Trade</p>
  </section>

  <section class="cover cover--red">
    <p class="author">Delphine Karsby</p>
    <h1 class="title"><span>Corsets,</span><span>Cups</span><span>&amp; Commerce</span></h1>
    <div class="tagline-band"></div>
    <p class="tagline">Steady Lessons for Women in Trade</p>
    <div class="bra-mark" role="img" aria-label="Line icon of a lace bra hanging from the tagline band"></div>
  </section>
</main>
</body>
</html>
```